July 2022 Industrial Manufacturer Product Expo Mexico City

We manufacture large screws and fastners for large Mining equipment, Trains, large ships, airplanes, wind turbines, and so on. We also do custom work base on the customer needs. No matter the size we can make it.
We have a Expo coming up with companies all over the world. We have to stand out we are a family own business so our customer service will be above and beyond anyone can provide. We do not have a sales force to push our products and services we provide one on one service.
Plus@!! I'm looking for anything that you designers can come up with if it was your company to put on a business card, plus i want to do a 1 or 2 sided pamphlet, and then a website. We make Speciality Bolts for large mining equipment these bolts can be 3 to 4 foot long!!! Plus fasteners, Nuts, washers, any, size, strengths, special materials, we offer more of a ono on one customer service, We are a small company, family own, but can fulfill any type of orders. We can also provide special time lines for emergency orders. "We keep the machines running we here at KRV don't believe in down time" We want to hear any slogan based on our company to stand out.
Thanks i really appreciate all your work and options that we have to pick on. Plus just a thought we could possibly want to entertain a experience Marketing internet help maybe a employment possibility. Thanks
Updates

I need 2 cards one in Spanish and English Like the steel back ground maybe send me in some bright red and blue writing Same with the Black cards Please remove the word Military The logo KRV maybe integrate a picture of a Bolt 🔩 Thank you

Still looking for I need 2 cards one in Spanish and English Like the steel back ground maybe send me in some bright red and blue writing Same with the Black cards try bright writing Please remove the word Military The logo KRV maybe integrate a picture of a Bolt 🔩 Plus will need the company to make a brochure and website next Thank you

Target Market(s)

Large Mining, Ship, Train, Green Energy, ORBA, and Government equipment. Throughout the World

Industry/Entity Type

We can Custom Manufacture any type of Fastners for Mining equipment, Trains, Ships, Green energy, Governments, or military projects. wind turbines,

Contact Information for Business Card

I attached the name and contact info that's on a card, plus the Company Logo. Would like industrial looking background with Bright Colors that will stand out!! If we can insert somewhere maybe on back that we "Custom Manufacture Any Size or Quantity Fastners for Large Mining Equipment, Trains, Ships, Green Energy Equipment or Government Projects

Font styles to use
Other font styles liked:
• You Pick, has to be bold, colorful standout, Professional looking Beable to read it.

Colors

Designer to choose colors to be used in the design.

Requirements
Must have
• Need in Spanish and English TO STANDOUT FROM THE REST OF THE EXPO!! See Business card details, Rounded corners
Nice to have
• Can i see some of the darker cards with Bright Red and Blue letters I like to see the different type of card material, heavy thickness, plastic, transparent, Metal types, Bright Colors, I saw like Raised letters like on the logo.

```html
<!DOCTYPE html>
<html lang="es">
<head>
<meta charset="utf-8">
<title>KRV – Tarjetas de presentación</title>
<link rel="stylesheet" href="https://fonts.googleapis.com/css2?family=Montserrat:wght@500;600;700;800&display=swap">
<style>
  :root {
    --stage: #2b2b2d;
    --card-black: #151516;
    --navy: #23307a;
    --royal: #1565c8;
    --sky: #1b8fe0;
    --ice: #d3ecfa;
    --ink: #111111;
    --steel: #3a3a3c;
    --silver: #d9d9db;
    --white: #ffffff;
  }
  * { margin: 0; padding: 0; box-sizing: border-box; }
  html, body {
    width: 1200px;
    height: 1108px;
    overflow: hidden;
    background: var(--stage);
    font-family: "Montserrat", sans-serif;
  }
  .card-set {
    position: relative;
    width: 1200px;
    height: 1108px;
  }
  .card {
    position: absolute;
    top: 174px;
    width: 460px;
    height: 760px;
    border-radius: 26px;
    overflow: hidden;
  }
  .card--back {
    left: 100px;
    background: var(--card-black);
    display: flex;
    flex-direction: column;
    align-items: center;
    justify-content: center;
  }
  .card--front { left: 640px; background: var(--white); }
  .card--front svg { display: block; }

  .back-brand {
    color: var(--silver);
    font-weight: 800;
    font-size: 104px;
    letter-spacing: 6px;
    line-height: 1;
  }
  .back-tagline {
    margin-top: 14px;
    color: var(--silver);
    font-weight: 500;
    font-size: 15px;
    letter-spacing: 0.5px;
  }
  .front-brand { font-weight: 800; font-size: 112px; letter-spacing: 6px; fill: var(--steel); }
  .front-tagline { font-weight: 600; font-size: 17px; fill: var(--navy); }
  .holder-name { font-weight: 700; font-size: 15px; fill: var(--white); letter-spacing: 0.5px; }
  .contact-text { font-weight: 500; font-size: 18px; fill: var(--ink); }
  .contact-icon { fill: var(--sky); }
  .rule { stroke: var(--ink); stroke-width: 1.4; }
</style>
</head>
<body>
<main class="card-set">

  <section class="card card--back" aria-label="Reverso de la tarjeta">
    <div class="back-brand">KRV</div>
    <div class="back-tagline">Fabricación Y distribución de tornillos</div>
  </section>

  <section class="card card--front" aria-label="Frente de la tarjeta">
    <svg width="460" height="760" viewBox="0 0 460 760" xmlns="http://www.w3.org/2000/svg">
      <defs>
        <linearGradient id="topBlue" x1="0" y1="1" x2="1" y2="0">
          <stop offset="0" stop-color="var(--sky)"/>
          <stop offset="1" stop-color="var(--navy)"/>
        </linearGradient>
        <linearGradient id="bottomBlue" x1="0" y1="1" x2="1" y2="0">
          <stop offset="0" stop-color="var(--sky)"/>
          <stop offset="1" stop-color="var(--navy)"/>
        </linearGradient>
      </defs>

      <polygon class="band-top" points="0,0 460,0 460,70 0,300" fill="url(#topBlue)"/>
      <polygon class="band-light" points="0,300 460,70 460,330 0,560" fill="var(--ice)"/>
      <polygon class="band-name" points="0,560 460,330 460,364 0,594" fill="var(--ink)"/>
      <polygon class="band-bottom" points="460,600 460,760 140,760" fill="url(#bottomBlue)"/>

      <line class="rule" x1="0" y1="640" x2="460" y2="410"/>
      <line class="rule" x1="0" y1="690" x2="460" y2="460"/>
      <line class="rule" x1="0" y1="740" x2="460" y2="510"/>
      <line class="rule" x1="40" y1="770" x2="460" y2="560"/>

      <text class="front-brand" transform="translate(92 398) rotate(-26.565)">KRV</text>
      <text class="front-tagline" transform="translate(112 476) rotate(-26.565)">Fabricación Y distribución de tornillos</text>

      <text class="holder-name" transform="translate(36 566) rotate(-26.565)">LIC. MARIANA ESTELA RUIZ VEGA</text>

      <g class="contact-row" transform="translate(60 598) rotate(-26.565)">
        <path class="contact-icon" d="M2 2 l4 -1 l3 5 l-2 2 a10 10 0 0 0 5 5 l2 -2 l5 3 l-1 4 a4 4 0 0 1 -4 2 a17 17 0 0 1 -14 -14 a4 4 0 0 1 2 -4z" transform="translate(0 -16) scale(0.8)"/>
        <text class="contact-text" x="24" y="0">Oficina 871 555 0142</text>
      </g>
      <g class="contact-row" transform="translate(76 640) rotate(-26.565)">
        <rect x="1" y="-17" width="12" height="18" rx="2" fill="none" stroke="var(--sky)" stroke-width="2.4"/>
        <text class="contact-text" x="24" y="0">8715550187</text>
      </g>
      <g class="contact-row" transform="translate(92 682) rotate(-26.565)">
        <rect class="contact-icon" x="0" y="-13" width="16" height="11"/>
        <polyline points="0,-13 8,-7 16,-13" fill="none" stroke="var(--white)" stroke-width="1.4"/>
        <text class="contact-text" x="24" y="0">tornilleriakrv.ventas@correo.com</text>
      </g>
    </svg>
  </section>

</main>
</body>
</html>
```